Door Hanger for Bright Harbor Painters

Design a double-sided door hanger that reinforces Bright Harbor Painters’ brand identity while promoting our interior painting services. This piece will be distributed in residential neighborhoods during the winter and should make a strong visual impression at a glance while offering enough detail to motivate follow-up. See attached design brief.

```html
<!DOCTYPE html>
<html lang="en">
<head>
<meta charset="utf-8">
<title>Bright Harbor Painters – Door Hanger</title>
<link href="https://fonts.googleapis.com/css2?family=Krona+One&family=Poppins:wght@400;500;600;700&display=swap" rel="stylesheet">
<style>
  :root{
    --green:#7a9a5c;
    --grey:#4f5350;
    --ink:#1f2120;
    --white:#ffffff;
    --stage:#000000;
  }
  *{margin:0;padding:0;box-sizing:border-box}
  html,body{width:1097px;height:1200px;overflow:hidden;background:var(--stage)}
  body{position:relative;font-family:"Poppins",sans-serif}
  .hanger{position:absolute;top:110px;width:379px;height:980px;background:var(--white);overflow:hidden}
  .hanger--front{left:132px}
  .hanger--back{left:586px}
  .hanger__top{position:absolute;left:0;top:0;width:379px;height:280px}
  .abs{position:absolute}
  .brand{left:0;width:379px;top:230px;display:flex;flex-direction:column;align-items:center;gap:6px}
  .brand__dot{width:34px;height:34px;border-radius:50%;background:var(--grey)}
  .brand__name{font-family:"Krona One",sans-serif;font-size:17px;line-height:21px;color:var(--grey);text-align:center;letter-spacing:.5px}
  .headline{font-family:"Krona One",sans-serif;text-align:center;left:0;width:379px;color:var(--grey);white-space:nowrap}
  .headline--front{top:337px;font-size:39px;line-height:37px}
  .headline--back{top:206px;font-size:32px;line-height:30px}
  .headline .accent{color:var(--green)}
  .pill{display:flex;align-items:center;justify-content:center;border-radius:16px;color:var(--white);font-weight:500;white-space:nowrap}
  .pill--grey{background:var(--grey)}
  .pill--green{background:var(--green)}
  .tagline{left:55px;width:264px;top:453px;height:29px;font-size:12px}
  .tagline--back{left:58px;top:303px;height:28px}
  .photo{border-radius:5px;background:linear-gradient(160deg,#e9e3da,#b99a78 60%,#5b4636)}
  .frame{border-radius:6px;padding:7px}
  .frame--grey{background:var(--grey)}
  .frame--green{background:var(--green)}
  .frame .photo{width:100%;height:100%}
  .illustration{left:53px;top:747px;width:286px;height:104px;background:linear-gradient(100deg,#8fcf9a,#c7e06a 45%,#b87a4d 75%,#6a3a20)}
  .address{left:31px;width:318px;top:851px;height:28px;font-size:13.5px;letter-spacing:.6px}
  .phone{left:0;width:379px;top:882px;text-align:center;font-weight:600;font-size:47px;line-height:52px;color:var(--green);letter-spacing:-.5px;white-space:nowrap}
  .email{left:0;width:379px;top:938px;text-align:center;font-size:17px;letter-spacing:4.6px;color:var(--grey);font-weight:500;white-space:nowrap}
  .about{left:33px;width:314px;top:348px;font-size:9.6px;line-height:12.6px;color:var(--ink);text-align:justify}
  .about p{margin-bottom:8px}
  .thumbs{left:33px;top:584px;width:314px;height:99px;display:flex;gap:8px}
  .thumbs .frame{flex:1;padding:6px}
  .services{left:33px;top:705px;width:314px}
  .services__title{height:27px;font-size:14.5px;border-radius:14px;margin-bottom:7px}
  .services__row{display:flex;gap:7px;margin-bottom:7px}
  .chip{flex:auto;height:27px;font-size:14px;border-radius:14px;background:var(--green);color:var(--white);display:flex;align-items:center;justify-content:center;font-weight:500;white-space:nowrap;padding:0 10px}
</style>
</head>
<body>

<section class="hanger hanger--front">
  <svg class="hanger__top" viewBox="0 0 379 280">
    <defs>
      <linearGradient id="roomFront" x1="0" y1="0" x2="1" y2="1">
        <stop offset="0" stop-color="#9bb383"/>
        <stop offset=".5" stop-color="#4d6340"/>
        <stop offset="1" stop-color="#2c3a24"/>
      </linearGradient>
    </defs>
    <rect width="379" height="280" fill="url(#roomFront)" role="img" aria-label="Photo of a painted interior with a coffered ceiling and balcony"/>
    <polygon points="0,274 189,148 379,274 379,280 0,280" fill="var(--green)"/>
    <polygon points="0,283 189,157 379,283" fill="var(--white)"/>
    <circle cx="189" cy="78" r="58" fill="var(--stage)"/>
  </svg>

  <div class="abs brand">
    <span class="brand__dot"></span>
    <span class="brand__name">BRIGHT HARBOR<br>PAINTERS</span>
  </div>

  <h1 class="abs headline headline--front">INTERIOR<br>PAINTING<br><span class="accent">SERVICES</span></h1>
  <div class="abs pill pill--grey tagline">Trusted Local Professionals, Since 2005</div>

  <div class="abs frame frame--grey" style="left:32px;top:503px;width:186px;height:235px">
    <div class="photo" role="img" aria-label="Photo of a kitchen with timber beams and an island"></div>
  </div>
  <div class="abs frame frame--green" style="left:226px;top:503px;width:114px;height:114px">
    <div class="photo" role="img" aria-label="Photo of a modern staircase" style="background:linear-gradient(160deg,#f1eee8,#9a8a78 60%,#2e2a26)"></div>
  </div>
  <div class="abs frame frame--green" style="left:226px;top:623px;width:114px;height:115px">
    <div class="photo" role="img" aria-label="Photo of a white hallway with built-in cabinets" style="background:linear-gradient(160deg,#f4f2ee,#ddd6cc 60%,#c9a47a)"></div>
  </div>

  <div class="abs illustration" role="img" aria-label="Illustration of a paintbrush resting on green paint swatches"></div>

  <div class="abs pill pill--grey address">47 Linden Ave. Harborview, VT 05400</div>
  <div class="abs phone">802-555-0143</div>
  <div class="abs email">INFO@BHPAINTERS.COM</div>
</section>

<section class="hanger hanger--back">
  <svg class="hanger__top" viewBox="0 0 379 280">
    <defs>
      <linearGradient id="roomBack" x1="0" y1="0" x2="1" y2="1">
        <stop offset="0" stop-color="#a3b98a"/>
        <stop offset=".55" stop-color="#5f7a4a"/>
        <stop offset="1" stop-color="#2f6b55"/>
      </linearGradient>
    </defs>
    <rect width="379" height="280" fill="url(#roomBack)" role="img" aria-label="Photo of a vaulted great room with a ring chandelier and tall windows"/>
    <polygon points="0,274 189,148 379,274 379,280 0,280" fill="var(--green)"/>
    <polygon points="0,283 189,157 379,283" fill="var(--white)"/>
    <circle cx="189" cy="78" r="58" fill="var(--stage)"/>
  </svg>

  <h2 class="abs headline headline--back">FRESH<br><span class="accent">INTERIOR</span><br>PAINT!</h2>
  <div class="abs pill pill--green tagline tagline--back">Professional, Reliable Workmanship</div>

  <div class="abs about">
    <p>Bright Harbor Painters provides a full range of interior painting services for Vermont homes and businesses, taking pride in our clean, communicative workmanship, and friendly, professional tradespeople.</p>
    <p>From walls and ceilings to trim and cabinets, our friendly team of professionals is ready to handle all aspects of your project with care and attention to detail.</p>
    <p>Proudly serving Vermont homes and businesses since 2005 with quality finishes, exceptional customer service and reasonable rates.</p>
    <p>We are access specialists and can safely complete difficult projects including vaulted ceilings, great rooms, foyers and stairways.</p>
    <p>Setting a higher standard for workmanship, client experience and value.</p>
  </div>

  <div class="abs thumbs">
    <div class="frame frame--green"><div class="photo" role="img" aria-label="Photo of an open living area with a fireplace"></div></div>
    <div class="frame frame--green"><div class="photo" role="img" aria-label="Photo of a walk-in closet with white built-ins" style="background:linear-gradient(160deg,#f4f2ee,#dcd6cc 60%,#b98a5c)"></div></div>
    <div class="frame frame--green"><div class="photo" role="img" aria-label="Photo of a dining room with timber ceiling beams" style="background:linear-gradient(160deg,#e3d7c4,#a9773f 60%,#3a2d22)"></div></div>
  </div>

  <div class="abs services">
    <div class="pill pill--grey services__title">SERVICES</div>
    <div class="services__row"><span class="chip">WALLS</span><span class="chip">CEILINGS</span><span class="chip">TRIM &amp; DOORS</span></div>
    <div class="services__row"><span class="chip">KITCHENS &amp; CABINETS</span><span class="chip">HIGH ACCESS</span></div>
    <div class="services__row"><span class="chip">STAIRWAYS</span><span class="chip">DRYWALL REPAIR</span></div>
  </div>

  <div class="abs pill pill--grey address">47 Linden Ave. Harborview, VT 05400</div>
  <div class="abs phone">802-555-0143</div>
  <div class="abs email">INFO@BHPAINTERS.COM</div>
</section>

</body>
</html>
```